A3 Poster & DL Flyer Design Project

We need a poster and flyer designed to advertise a Wine, Food and Live music event.
Event title is "An Evening Under Vines" and is put on by Holloway's Ridge Wines. Date for the event is Sunday 21 April 2013
The outdoor event covers wine, gourmet food and live music
Live music genera is Jazz, Blues, Swing

Reason: Most of the designs did not meet our requirements only 3 out of 21 have potential but would like to see more

Target Market(s)

25 - 55 wine drinkers with money.

Industry/Entity Type

Event

Requirements
Must have
• Title of the Event "An Evening Under Vinez"
Date Sunday 21 April 2013 or be generic where we can write the date on each year.
Camel Logo
Entry is Free
No BYO Alcohol
Must reflect Wine, Food & Live Music

```html
<!DOCTYPE html>
<html lang="en">
<head>
<meta charset="utf-8">
<title>An Evening Under Vines – Event Flyer</title>
<link rel="stylesheet" href="https://fonts.googleapis.com/css2?family=Open+Sans:wght@300;400&family=Roboto+Condensed:wght@700&family=Arvo:wght@700&display=swap">
<style>
  :root {
    --page: #e4e4e4;
    --wine-deep: #2a0a08;
    --wine-mid: #6e1a12;
    --wine-warm: #8c2a1a;
    --plank-light: #dcb98c;
    --plank-mid: #c59a68;
    --plank-dark: #a47a4c;
    --rope: #c9a474;
    --ink: #141010;
    --badge-red: #a3161c;
    --badge-rim: #e9dada;
    --paper-white: #ffffff;
  }
  * { margin: 0; padding: 0; box-sizing: border-box; }
  html, body { width: 1200px; height: 800px; overflow: hidden; background: var(--page); }

  .flyer {
    position: absolute;
    left: 320px; top: 10px;
    width: 560px; height: 780px;
    overflow: hidden;
    background: linear-gradient(160deg, var(--wine-warm) 0%, var(--wine-mid) 40%, var(--wine-deep) 100%);
    box-shadow: 0 4px 16px rgba(0,0,0,.25);
  }

  .event-heading { position: absolute; left: 36px; top: 34px; color: var(--paper-white); }
  .event-title { font: 300 46px/1.05 "Open Sans", sans-serif; }
  .event-host { font: 400 22px/1.4 "Open Sans", sans-serif; margin-top: 6px; }

  .wine-photo {
    position: absolute; right: 0; top: 140px;
    width: 270px; height: 440px;
    background:
      radial-gradient(ellipse at 40% 22%, rgba(240,190,140,.55), transparent 45%),
      radial-gradient(ellipse at 65% 70%, rgba(200,190,90,.75), transparent 60%),
      linear-gradient(180deg, #7a2a18 0%, #9a6a3a 55%, #b8a060 100%);
    -webkit-mask-image: linear-gradient(90deg, transparent 0%, #000 30%);
            mask-image: linear-gradient(90deg, transparent 0%, #000 30%);
  }

  .feature-signs { position: absolute; left: 40px; top: 150px; width: 260px; list-style: none; }
  .feature-sign {
    position: relative;
    height: 62px; margin-top: 22px;
    border-radius: 8px 14px 10px 6px;
    background: linear-gradient(180deg, var(--plank-light), var(--plank-mid) 60%, var(--plank-dark));
    box-shadow: 0 3px 6px rgba(0,0,0,.45);
    display: flex; align-items: center; justify-content: center;
    font: 700 34px/1 "Roboto Condensed", sans-serif;
    color: var(--ink);
  }
  .feature-sign::before, .feature-sign::after {
    content: ""; position: absolute; top: -24px;
    width: 4px; height: 26px; background: var(--rope); border-radius: 2px;
  }
  .feature-sign::before { left: 24px; }
  .feature-sign::after { right: 24px; }

  .date-badge {
    position: absolute; left: 240px; top: 580px;
    width: 180px; height: 180px; border-radius: 50%;
    background: var(--badge-rim);
    padding: 8px;
  }
  .date-badge-inner {
    width: 100%; height: 100%; border-radius: 50%;
    background: radial-gradient(circle at 40% 30%, #c42026, var(--badge-red) 70%, #7e0f13);
    display: flex; flex-direction: column; align-items: center; justify-content: center;
    color: var(--paper-white);
    font: 700 30px/1.15 "Arvo", serif;
  }
  .date-badge-inner sup { font-size: 16px; }
</style>
</head>
<body>
  <main class="flyer">
    <header class="event-heading">
      <h1 class="event-title">An Evening Under Vines</h1>
      <p class="event-host">by Holloway's Ridge Wines</p>
    </header>

    <div class="wine-photo" role="img" aria-label="Photo of a glass of wine beside a bunch of green grapes"></div>

    <ul class="feature-signs">
      <li class="feature-sign">Wine</li>
      <li class="feature-sign">Gourmet Food</li>
      <li class="feature-sign">Live Music</li>
      <li class="feature-sign">Entry is Free</li>
      <li class="feature-sign">No BYO Alcohol</li>
    </ul>

    <div class="date-badge">
      <p class="date-badge-inner">
        <span>21<sup>st</sup></span>
        <span>APRIL</span>
        <span>2013</span>
      </p>
    </div>
  </main>
</body>
</html>
```